Kestrel Photography Business Card

I need a business card designed for a photography business based in Perth, Western Australia called Kestrel Photography.

We specialise in wedding, event photography and portrait photography.

The business card must borrow the style of the attached logo.

The hex codes for the colours in the logo are:
#ED1D85 - Pink
#89C23E - Green
#37282F - Black

The name on the card will be:
Name: Torvane
Phone: 0417395286
Website: www.kestrelphotography.example.au
Facebook: kestrelphotography

I am open and happy to accept creative concepts.

I’d like some space at the back for writing notes and appointment details.

```html
<!DOCTYPE html>
<html lang="en">
<head>
<meta charset="utf-8">
<title>Kestrel Photography Business Card</title>
<link href="https://fonts.googleapis.com/css2?family=Barlow:wght@300;400&display=swap" rel="stylesheet">
<style>
  :root {
    --pink: #ED1D85;
    --green: #89C23E;
    --ink: #37282F;
    --text: #5b5057;
    --rule: #8d8589;
    --card-edge: #4b4046;
    --card-face: #f3f3f2;
    --backdrop: #262626;
  }
  * { margin: 0; padding: 0; box-sizing: border-box; }
  html, body {
    width: 1200px; height: 900px; overflow: hidden;
    background: var(--backdrop);
    font-family: "Barlow", Arial, sans-serif;
  }
  .card {
    position: absolute; left: 355px; width: 486px; height: 270px;
    background: var(--card-edge); border-radius: 16px;
  }
  .card--front { top: 158px; }
  .card--back { top: 467px; }
  .card__face {
    position: absolute; left: 15px; top: 16px; right: 15px; bottom: 16px;
    background: var(--card-face);
    border: 1.5px solid var(--green);
    border-radius: 12px;
    overflow: hidden;
  }
  .brand-mark {
    position: absolute; border-radius: 50%; background: var(--pink);
  }
  .card--front .brand-mark { left: 62px; top: 60px; width: 60px; height: 60px; }
  .brand-name {
    position: absolute; left: 20px; top: 132px; width: 144px;
    text-align: center; font-weight: 400; font-size: 12px;
    letter-spacing: 1px; color: var(--ink); text-transform: uppercase;
  }
  .holder-name {
    position: absolute; left: 216px; top: 48px;
    font-size: 21px; font-weight: 400; letter-spacing: 1.2px; color: var(--text);
  }
  .contact { position: absolute; left: 215px; right: 10px; top: 114px; list-style: none; }
  .contact__item {
    display: flex; align-items: center; height: 30.5px;
    font-size: 11.5px; font-weight: 400; letter-spacing: 0.1px; color: var(--text);
    white-space: nowrap;
  }
  .contact__icon { width: 15px; height: 15px; margin-right: 9px; flex: none; }
  .card--back .brand-mark { left: 208px; top: 16px; width: 70px; height: 70px; }
  .studio-title {
    position: absolute; left: 0; right: 0; top: 111px;
    text-align: center; font-size: 13px; font-weight: 400;
    letter-spacing: 7.6px; color: var(--text); text-transform: uppercase;
  }
  .note-lines { position: absolute; left: 31px; right: 31px; top: 151px; }
  .note-lines__rule { height: 24.7px; border-top: 1px solid var(--rule); }
</style>
</head>
<body>
  <section class="card card--front">
    <div class="card__face">
      <div class="brand-mark"></div>
      <div class="brand-name">Kestrel Photography</div>
      <h1 class="holder-name">TORVANE</h1>
      <ul class="contact">
        <li class="contact__item">
          <svg class="contact__icon" viewBox="0 0 16 16" aria-hidden="true">
            <circle cx="8" cy="8" r="8" fill="#5b5057"/>
            <rect x="5" y="3.5" width="6" height="9" rx="1" fill="none" stroke="#fff" stroke-width="1.2"/>
            <circle cx="8" cy="10.8" r="0.7" fill="#fff"/>
          </svg>
          0417395286
        </li>
        <li class="contact__item">
          <svg class="contact__icon" viewBox="0 0 16 16" aria-hidden="true">
            <circle cx="8" cy="8" r="8" fill="#5b5057"/>
            <path d="M8 12.5 C6 10 5 8.6 5 7 A3 3 0 0 1 11 7 C11 8.6 10 10 8 12.5Z" fill="#fff"/>
            <circle cx="8" cy="7" r="1.1" fill="#5b5057"/>
          </svg>
          www.kestrelphotography.example.au
        </li>
        <li class="contact__item">
          <svg class="contact__icon" viewBox="0 0 16 16" aria-hidden="true">
            <circle cx="8" cy="8" r="8" fill="#5b5057"/>
          </svg>
          kestrelphotography
        </li>
      </ul>
    </div>
  </section>

  <section class="card card--back">
    <div class="card__face">
      <div class="brand-mark"></div>
      <h2 class="studio-title">Kestrel Photography</h2>
      <div class="note-lines">
        <div class="note-lines__rule"></div>
        <div class="note-lines__rule"></div>
        <div class="note-lines__rule"></div>
        <div class="note-lines__rule"></div>
      </div>
    </div>
  </section>
</body>
</html>
```